Business Card Design Project

we are a new company , see www.chatharborlane.com
we also have a concurrent flyer deign competition so you may also wish to enter that.
We provide live customer support services for websites.
We cater for mainly european market.
info for card:
Martin Colbrook
Director
p: +353 (0)90 612 8051
f: +353 (0)90 612 8062
m: +353 (0)86 507 4926
e: martin@chatharborlane.com
w: www.chatharborlane.com
The card does not have to use the exact colour on the website but should ahve something of the general feel of it. It should have modern corporate feel without brash coulours. we will upload the logo and card should be standard european size 85x55mm
Target Market(s)
Online business owners
Industry/Entity Type
Business
Look and feel
Each slider illustrates characteristics of the customer's brand and the style your logo design should communicate.

```html
<!DOCTYPE html>
<html lang="en">
<head>
<meta charset="utf-8">
<title>Chat Harbor Lane – Business Card</title>
<link rel="stylesheet" href="https://fonts.googleapis.com/css2?family=Exo+2:wght@400;500;600;700&display=swap">
<style>
  :root {
    --backdrop: #2282b0;
    --card: #6d6d6f;
    --accent: #5ec4ea;
    --ink: #ffffff;
    --brand-square: #2a86b8;
  }
  * { margin: 0; padding: 0; box-sizing: border-box; }
  html, body {
    width: 1161px;
    height: 1200px;
    overflow: hidden;
    background: var(--backdrop);
    font-family: "Exo 2", "Helvetica Neue", Arial, sans-serif;
  }
  .canvas {
    position: relative;
    width: 1161px;
    height: 1200px;
  }
  .card {
    position: absolute;
    left: 276px;
    width: 592px;
    height: 382px;
    background: var(--card);
    color: var(--ink);
  }
  .card--front { top: 167px; }
  .card--back  { top: 624px; }

  .brand {
    position: absolute;
    left: 0;
    right: 0;
    top: 162px;
    display: flex;
    align-items: center;
    justify-content: center;
    gap: 14px;
  }
  .brand__mark {
    width: 40px;
    height: 40px;
    background: var(--brand-square);
  }
  .brand__name {
    font-size: 38px;
    font-weight: 700;
    letter-spacing: 1px;
    text-transform: uppercase;
    color: var(--ink);
    line-height: 1;
  }

  .person {
    position: absolute;
    left: 48px;
    top: 67px;
  }
  .person__name {
    font-size: 23px;
    font-weight: 600;
    color: var(--accent);
    line-height: 1.1;
  }
  .person__role {
    font-size: 16px;
    font-weight: 400;
    color: var(--ink);
    margin-top: 1px;
  }

  .contact {
    position: absolute;
    top: 270px;
    list-style: none;
    font-size: 15.5px;
    line-height: 21px;
  }
  .contact--phones { left: 48px; }
  .contact--online { left: 304px; }
  .contact__item { display: flex; white-space: nowrap; }
  .contact__label {
    width: 26px;
    text-align: center;
    color: var(--accent);
    font-weight: 500;
  }
  .contact__value { color: var(--ink); }
</style>
</head>
<body>
<main class="canvas">
  <section class="card card--front" aria-label="Card front">
    <div class="brand">
      <span class="brand__mark" aria-hidden="true"></span>
      <span class="brand__name">Chat Harbor Lane</span>
    </div>
  </section>

  <section class="card card--back" aria-label="Card back">
    <div class="person">
      <p class="person__name">Martin Colbrook</p>
      <p class="person__role">Director</p>
    </div>

    <ul class="contact contact--phones">
      <li class="contact__item"><span class="contact__label">P</span><span class="contact__value">+353 (0) 90 612 8051</span></li>
      <li class="contact__item"><span class="contact__label">F</span><span class="contact__value">+353 (0) 90 612 8062</span></li>
      <li class="contact__item"><span class="contact__label">M</span><span class="contact__value">+353 (0) 86 507 4926</span></li>
    </ul>

    <ul class="contact contact--online">
      <li class="contact__item"><span class="contact__label">E</span><span class="contact__value">martin@chatharborlane.com</span></li>
      <li class="contact__item"><span class="contact__label">W</span><span class="contact__value">www.chatharborlane.com</span></li>
    </ul>
  </section>
</main>
</body>
</html>
```